Business Card, Stationary Folder & Envelope
ORVALUX
Creative Brief
Bright & Fun-filled
Ramiro Quesada
TRL
Carretera Pueblanco - Ozumel Km 3.4, Colonia El Prado Tepalcingo, P.C. 90487, Tlaxcala, Tlax., México
VOXEL ID 57*83*40962
ramiro.quesada@orvalux.example
www.orvalux.example

```html
<!DOCTYPE html>
<html lang="es">
<head>
<meta charset="utf-8">
<title>ORVALUX — Business Cards</title>
<link rel="stylesheet" href="https://fonts.googleapis.com/css2?family=Arimo:wght@400;700&display=swap">
<style>
  :root {
    --backdrop: #ebe6df;
    --card-white: #fbfbfb;
    --brand-blue: #4fb3e8;
    --brand-grey: #7b7e83;
    --text-grey: #5f6266;
    --white: #ffffff;
  }
  * { box-sizing: border-box; margin: 0; padding: 0; }
  html, body { width: 1200px; height: 761px; overflow: hidden; }
  body {
    position: relative;
    background: var(--backdrop);
    font-family: "Arimo", Arial, sans-serif;
    color: var(--text-grey);
  }
  .card {
    position: absolute;
    width: 500px;
    height: 278px;
    border-radius: 12px;
    box-shadow: 0 6px 18px rgba(0,0,0,0.18);
    overflow: hidden;
  }
  .card-front { left: 103px; top: 160px; background: var(--card-white); padding: 24px 40px; }
  .card-back-blue { left: 648px; top: 65px; background: var(--brand-blue); }
  .card-back-white { left: 391px; top: 440px; background: var(--card-white); }

  .wordmark { display: flex; align-items: center; gap: 12px; }
  .wordmark-dot { width: 30px; height: 30px; border-radius: 50%; background: var(--brand-blue); flex: none; }
  .wordmark-name { font-weight: 700; font-size: 44px; letter-spacing: 1px; color: var(--brand-grey); line-height: 1; }
  .tagline { margin: 4px 0 0 130px; font-size: 13px; font-weight: 700; letter-spacing: 1.5px; color: var(--brand-grey); }

  .person { margin-top: 20px; }
  .person-name { font-size: 20px; font-weight: 700; color: var(--brand-blue); }
  .person-role { font-size: 11px; margin-top: 2px; }
  .address { margin-top: 16px; font-size: 11px; line-height: 1.45; }
  .contact { margin-top: 12px; font-size: 11px; line-height: 1.45; }

  .back-center {
    position: absolute; inset: 0;
    display: flex; flex-direction: column; align-items: center; justify-content: center;
  }
  .back-mark { display: flex; align-items: center; gap: 14px; margin-top: -20px; }
  .back-mark .wordmark-dot { width: 40px; height: 40px; }
  .back-mark .wordmark-name { font-size: 48px; }
  .card-back-blue .wordmark-dot { background: var(--white); }
  .card-back-blue .wordmark-name { color: var(--white); }
  .web {
    margin-top: 52px; font-size: 21px; font-weight: 700; letter-spacing: 2px;
  }
  .card-back-blue .web { color: var(--white); }
  .card-back-white .web { color: var(--brand-blue); }
</style>
</head>
<body>
  <section class="card card-front">
    <div class="wordmark">
      <span class="wordmark-dot"></span>
      <span class="wordmark-name">ORVALUX</span>
    </div>
    <p class="tagline">STAMPING SOLUTIONS</p>
    <div class="person">
      <p class="person-name">Ramiro Quesada</p>
      <p class="person-role">TRL</p>
    </div>
    <address class="address" style="font-style:normal">
      Carretera Pueblanco - Ozumel Km 3.4<br>
      Colonia El Prado Tepalcingo<br>
      P.C. 90487, Tlaxcala, Tlax., México
    </address>
    <p class="contact">
      VOXEL ID 57*83*40962 &nbsp;|&nbsp; P: +52 (246) 310-4827<br>
      C: +52 (222) 718 42 60 &nbsp;|&nbsp; F: +52 (246) 310-5512<br>
      ramiro.quesada@orvalux.example &nbsp;|&nbsp; www.orvalux.example
    </p>
  </section>

  <section class="card card-back-blue">
    <div class="back-center">
      <div class="back-mark">
        <span class="wordmark-dot"></span>
        <span class="wordmark-name">ORVALUX</span>
      </div>
      <p class="web">www.orvalux.example</p>
    </div>
  </section>

  <section class="card card-back-white">
    <div class="back-center">
      <div class="back-mark">
        <span class="wordmark-dot"></span>
        <span class="wordmark-name">ORVALUX</span>
      </div>
      <p class="web">www.orvalux.example</p>
    </div>
  </section>
</body>
</html>
```